Following list to be designed:

1. A4 Letter Head

Must comprise of:
BRISK HARBOR and its LOGO
Address: No.41, 2F, Telvin Court, Marlow Lane, Upper Fennel Gardens, Bangalore 560 078
Tel: 080 41927380
Fax: 080 41927381
Mail: hello@briskharbor.example

Color of wordings to be in the lighter shade of blue and brighter shade of blue.

2. A4 Envelope

Must comprise of:
BRISK HARBOR and its LOGO
Tel: 080 41927380
Fax: 080 41927381

3. Postal Envelope

Must comprise of:
BRISK HARBOR and its LOGO
Tel: 080 41927380
Fax: 080 41927381

4. Business Card

Must comprise of:
Ravi Menon
Managing Partner
Cell: +91 9847162053
Mail: ravimenon@briskharbor.example
Tel: 080 41927380
Fax: 080 41927381

5. A4 Letter Head

Must comprise of:
BRISK HARBOR CORP. (wording) and BRISK HARBOR LOGO (only blue ribbon)

Blue ribbon (BRISK HARBOR LOGO) may be placed on Left Top Corner of the A4 Letter Head
and BRISK HARBOR CORP. (wording) to be placed on Right Top Corner of the A4 Letter Head

Tel: 080 41927380
Fax: 080 41927381

6. . A4 Envelope

Must comprise of:

Blue ribbon (BRISK HARBOR LOGO) may be placed on Left Top Corner of the A4 Envelope
and BRISK HARBOR CORP. (wording) to be placed on Right Top Corner of the A4 Envelope
Tel: 080 41927380
Fax: 080 41927381

Target Market(s)

Top IT/ITES Organizations

Industry/Entity Type

Real Estate Development

Font styles to use
Serif
Sans Serif

Colors
33a6d7
0792cd
85cae6

Requirements
Should not have
• Playful font and color

```html
<!DOCTYPE html>
<html lang="en">
<head>
<meta charset="utf-8">
<title>Brisk Harbor Stationery</title>
<link href="https://fonts.googleapis.com/css2?family=Montserrat:wght@400;600;700&family=Open+Sans:wght@400;600&display=swap" rel="stylesheet">
<style>
:root{
  --bg:#eef0f2;
  --paper:#ffffff;
  --blue-bright:#0792cd;
  --blue-mid:#33a6d7;
  --blue-light:#85cae6;
  --ink:#3a3f45;
  --ink-soft:#6b7178;
  --faint:#e6f1f7;
}
*{margin:0;padding:0;box-sizing:border-box}
html,body{width:1200px;height:863px;overflow:hidden;background:var(--bg)}
body{position:relative;font-family:"Open Sans",Arial,sans-serif;color:var(--ink)}

.brand{display:flex;align-items:center;gap:8px}
.brand-dot{width:22px;height:22px;border-radius:50%;background:var(--blue-bright)}
.brand-name{font-family:"Montserrat",Arial,sans-serif;font-weight:600;letter-spacing:1px;color:var(--blue-bright);font-size:15px}

/* Letterhead */
.letterhead{position:absolute;left:70px;top:28px;width:572px;height:808px;background:var(--paper);box-shadow:0 4px 14px rgba(0,0,0,.12);overflow:hidden}
.letterhead .brand{position:absolute;top:40px;left:0;right:0;justify-content:center}
.letterhead-watermark{position:absolute;right:-90px;bottom:70px;width:380px;height:380px;border-radius:50%;background:var(--faint)}
.letter{position:absolute;left:60px;top:120px;width:430px;font-size:10px;line-height:1.55;color:var(--ink)}
.letter p{margin-bottom:12px}
.letter .recipient{margin-bottom:14px}
.signature{width:110px;height:34px;margin:6px 0 2px;background:linear-gradient(90deg,#d9dde1,#eef0f2);border-radius:4px}
.sign-title{font-weight:600}
.letterhead-footer{position:absolute;right:40px;bottom:32px;text-align:right;font-size:8.5px;line-height:1.7}
.letterhead-footer .address{color:var(--blue-light)}
.letterhead-footer .contacts{color:var(--blue-bright)}

/* Business cards */
.card{position:absolute;width:420px;height:240px;box-shadow:0 4px 14px rgba(0,0,0,.14);overflow:hidden}
.card-back{left:720px;top:110px;background:var(--paper)}
.card-back .brand{position:absolute;left:34px;top:40px}
.card-contacts{position:absolute;left:262px;top:36px;list-style:none;font-size:8.5px;line-height:2;color:var(--ink-soft)}
.card-contacts li{display:flex;align-items:center;gap:7px}
.card-contacts svg{width:10px;height:10px;fill:var(--blue-bright)}
.card-person{position:absolute;left:34px;top:128px}
.person-name{font-family:"Montserrat",Arial,sans-serif;font-weight:700;font-size:13px;letter-spacing:1px;color:var(--blue-bright)}
.person-role{font-size:9px;color:var(--blue-mid);margin-bottom:8px}
.person-address{font-size:8px;line-height:1.5;color:var(--ink-soft);width:190px}

.card-front{left:720px;top:450px;background:var(--blue-bright)}
.card-front-watermark{position:absolute;left:-60px;top:-40px;width:260px;height:260px;border-radius:50%;background:rgba(255,255,255,.08)}
.card-front .brand{position:absolute;left:0;right:0;top:108px;justify-content:center}
.card-front .brand-dot{background:#fff}
.card-front .brand-name{color:#fff;font-size:20px}
</style>
</head>
<body>

<section class="letterhead">
  <div class="letterhead-watermark"></div>
  <div class="brand"><span class="brand-dot"></span><span class="brand-name">BRISK HARBOR</span></div>
  <div class="letter">
    <p class="recipient">November 1, 2015<br>Mr. Tomas Reyner<br>56 Alder Crest Lane<br>Harlow Park 560045</p>
    <p>Dear Mr. Reyner:</p>
    <p>The opening paragraph of this letter states its main point. We thank you for your interest in our workspace portfolio and outline here how our team can support your coming expansion plans in the city.</p>
    <p>The second paragraph gives the supporting details. Our sites offer flexible floor plates, reliable power, secure access and quick links to the main transit corridors, which suit growing technology teams well.</p>
    <p>In closing, we restate our purpose and invite a site visit at a time that suits you. Please reach us through the contact details below so we can arrange a short walkthrough.</p>
    <p>Thank you for your time and consideration. We look forward to working with you.</p>
    <p>Sincerely,</p>
    <div class="signature" role="img" aria-label="Handwritten signature"></div>
    <div class="sign-title">President</div>
  </div>
  <footer class="letterhead-footer">
    <div class="address">No.41, 2F, Telvin Court, Marlow Lane, Upper Fennel Gardens, Bangalore 560 078</div>
    <div class="contacts">Tel: 080 41927380 &nbsp;|&nbsp; Fax: 080 41927381 &nbsp;|&nbsp; Email: hello@briskharbor.example</div>
  </footer>
</section>

<section class="card card-back">
  <div class="brand"><span class="brand-dot"></span><span class="brand-name">BRISK HARBOR</span></div>
  <ul class="card-contacts">
    <li><svg viewBox="0 0 10 10"><rect x="3" y="0.5" width="4" height="9" rx="1"/></svg>+91 9847162053</li>
    <li><svg viewBox="0 0 10 10"><path d="M2 1l2 0 1 2-1 1a5 5 0 0 0 2 2l1-1 2 1 0 2c-4 1-8-3-7-7z"/></svg>080 41927380</li>
    <li><svg viewBox="0 0 10 10"><rect x="1" y="3" width="8" height="5" rx="1"/><rect x="3" y="1" width="4" height="2"/></svg>080 41927381</li>
    <li><svg viewBox="0 0 10 10"><rect x="0.5" y="2" width="9" height="6" rx="1"/></svg>ravimenon@briskharbor.example</li>
  </ul>
  <div class="card-person">
    <div class="person-name">RAVI MENON</div>
    <div class="person-role">Managing Partner</div>
    <div class="person-address">No.41, 2F, Telvin Court, Marlow Lane, Upper Fennel Gardens, Bangalore 560 078</div>
  </div>
</section>

<section class="card card-front">
  <div class="card-front-watermark"></div>
  <div class="brand"><span class="brand-dot"></span><span class="brand-name">BRISK HARBOR</span></div>
</section>

</body>
</html>
```